Calloway Aeronautics website

We are an aviation company based in Miramar, FL but with worldwide coverage. We are involved in commercial aircraft (mostly freighters) trading, sale & leasing. Specifically, we specialized in freighters of the Vantrex family (V310, V320, V330, V340, V350). We also assist with financing, sale/leaseback. Handle special aviation projects and provide consultancy services. Currently engaged in a Vantrex 350 passenger to Freighter conversion (P2F).

Website Preliminary Initial Content/Sections as follows:

About Us
Founded in 2011, Calloway Aeronautics' management has many years of experience in Aviation, a strong background in scheduled airlines with emphasis in all cargo operations, freight forwarding supply chain and freight logistics, as well as ACMI and CMI operations.

Calloway’s focuses in facilitating wet and dry lease operations, charter and ACMI programs consultancy, aircraft sales, leasing and procurement, aviation consultancy and aircraft management.

Calloway team is a hands-on reliable alternative that works toward achieving your aircraft and aviation objectives by meeting your requirements and timeframe throughout professional and personalized service.

Teodoro Lasalle has over three decades of experience in the aviation field including aircraft maintenance, airline management, supply chain and logistics management. Teodoro is a true entrepreneur with proven experience and expertise on the multiple facets of the commercial aviation industry throughout the creation and development of a cluster of aviation entities. Teodoro is the founder and former sole member/chairman of 64 Jet, a Vantrex 340 All-Cargo U.S. Certificated Air Carrier created from scratch in 2014 which nowadays conforms a superb growing airline platform with an immaculate compliance operational record.

Services

Aircraft Finance, Trading, Procurement and Leasing
Calloway buys, sells, leases and facilitates aircraft trading while specializes in structured aircraft investment projects. Calloway has deep industry relationships and years of expertise, allowing to successfully execute lease transactions. We assist airlines, financial institutions and leasing companies when selling or purchasing aircraft.

Aircraft Available for Sale/Lease

Sale/Leaseback
Sale-leaseback is a method of financing. If your company needs liquidity, your aircraft or engine can serve as collateral for a loan throughout a sale-leaseback transaction. Sale-leaseback can free the equity tied up in aircraft or asset. Even if there is no pressing need for funds, a sale-leaseback allows you to use the equity tied up in your aircraft in a more productive fashion. Leaseback arrangements are usually employed because they confer financing, accounting or taxation benefits.

Passenger to Freighter Conversion (P2F)
Pandemic has seen the resurgence of operators packing freight into the main cabins of passenger aircraft. Carriers have been allowed to transport cargo in the cabin by removing passenger seats completely. NCA/ORSA have established exemptions that allow operators to fly in “Preighter” configuration for a limited time. Calloway is closely working with a U.S. group that is developing a Class E Supplemental Type Certificate (STC) for applicability on V350 aircraft which will include a cargo door for containerized freight. Final approvals are expected during first quarter of 2022.
Wet lease
Throughout our deep relationships within the industry, Calloway facilitates short or long-term wet leases to airlines and qualified parties around the globe, whereby we provide the Aircraft, Crews, Maintenance and Insurance (ACMI) worldwide services at competitive rates. We also specialize in AM leases where the aircraft is registered onto Lessee´s AOC with all maintenance services included in the rates, covering all maintenance risks, or CM or CMI where the client provides the aircraft.

Dry Lease
We offer aircraft from our own portfolio on dry lease or could engage in procuring the aircraft of your choice.

Asset & Aircraft Management
We provide aircraft owners Aircraft Management services, where we manage the technical side of the aircraft or the asset. Calloway also provides Harwick Dynamo engines trading, repair and full management services. We also buy Vantrex/Skylane surplus inventory.

Worldwide Charters
We facilitate the arrangement of full charters to airlines and logistics companies. Certain territory restrictions may apply.

Aviation Consultancy
We provide airline consultancy services for new or special projects. Calloway also specializes on All Cargo International route analysis, implementation and development. Our team provides professional guidance in obtaining worldwide both scheduled and charter authority.

Target Market(s)

Our target market are the airlines, logistics companies and commercial aviation related entities

Industry/Entity Type

Commercial Aviation

Coding

Number of Pages Required

3 page

Requirements
Must have
• Illustrations of wide body freighters such V350, V340, V320

```html
<!DOCTYPE html>
<html lang="en">
<head>
<meta charset="utf-8">
<title>Calloway Aeronautics</title>
<link rel="stylesheet" href="https://fonts.googleapis.com/css2?family=Fjalla+One&family=Outfit:wght@400;500;600&display=swap">
<style>
  :root {
    --sky-top: #43b3f7;
    --sky-bottom: #84d0fa;
    --navy: #0a1440;
    --ink: #0d1530;
    --white: #ffffff;
    --accent: #e8582a;
    --art-cream: #efe3c9;
    --art-orange: #e46a45;
    --art-navy: #1b2a4f;
  }
  * { margin: 0; padding: 0; box-sizing: border-box; }
  html, body { width: 1200px; height: 849px; overflow: hidden; }
  body {
    background: linear-gradient(180deg, var(--sky-top) 0%, var(--sky-bottom) 100%);
    font-family: "Outfit", sans-serif;
    color: var(--ink);
    position: relative;
  }
  .site-header { position: absolute; inset: 0 0 auto 0; height: 150px; }
  .brand {
    position: absolute; left: 201px; top: 8px; width: 133px; height: 133px;
    background: var(--navy);
    display: flex; align-items: center; justify-content: center; text-align: center;
  }
  .brand-name {
    color: var(--white); font-family: "Outfit", sans-serif; font-weight: 400;
    font-size: 11px; letter-spacing: 1.5px; line-height: 1.4; text-transform: uppercase;
  }
  .main-nav {
    position: absolute; left: 632px; top: 74px;
    display: flex; gap: 14px;
  }
  .main-nav a {
    color: var(--white); text-decoration: none; font-weight: 600; font-size: 13.5px;
  }
  .main-nav a.is-current { color: var(--navy); }

  .hero { position: absolute; left: 0; top: 0; width: 1200px; height: 560px; }
  .hero-art {
    position: absolute; left: 90px; top: 330px; width: 1020px; height: 222px;
    border-radius: 6px;
    background: linear-gradient(90deg, rgba(239,227,201,.55) 0%, rgba(228,106,69,.35) 55%, rgba(27,42,79,.25) 100%);
  }
  .hero-title {
    position: absolute; left: 0; width: 1200px; top: 184px; text-align: center;
    font-family: "Fjalla One", sans-serif; font-weight: 400; font-size: 42px;
    color: var(--navy); line-height: 1.1;
  }
  .hero-lead {
    position: absolute; left: 0; width: 1200px; top: 240px; text-align: center;
    font-size: 16px; line-height: 20.5px; color: var(--ink);
  }
  .hero-button {
    position: absolute; left: 532px; top: 292px; width: 116px; height: 24px;
    border: 1.2px solid var(--navy); color: var(--navy);
    font-size: 11px; letter-spacing: 1.2px; font-weight: 500;
    display: flex; align-items: center; justify-content: center; text-decoration: none;
  }

  .services-intro { position: absolute; left: 0; width: 1200px; top: 616px; text-align: center; }
  .services-title {
    font-family: "Fjalla One", sans-serif; font-weight: 400; font-size: 42px;
    color: var(--accent); line-height: 1.1;
  }
  .services-text {
    width: 700px; margin: 12px auto 0; font-size: 13px; line-height: 16.5px; color: var(--ink);
  }
</style>
</head>
<body>
  <header class="site-header">
    <div class="brand"><span class="brand-name">Calloway<br>Aeronautics</span></div>
    <nav class="main-nav">
      <a href="#" class="is-current">Home</a>
      <a href="#">About us</a>
      <a href="#">Services</a>
      <a href="#">Sale/Leaseback</a>
    </nav>
  </header>

  <section class="hero">
    <div class="hero-art" role="img" aria-label="Flat illustration of a wide body freighter being loaded with cargo pallets by ground vehicles on the apron"></div>
    <h1 class="hero-title">Calloway Aeronautics'</h1>
    <p class="hero-lead">We are an aviation company based in Miramar, FL<br>but with worldwide coverage.</p>
    <a href="#" class="hero-button">LEARN MORE</a>
  </section>

  <section class="services-intro">
    <h2 class="services-title">Services</h2>
    <p class="services-text">Calloway buys, sells, leases and facilitates aircraft trading while specializes in structured aircraft investment projects. Calloway has deep industry relationships and years of expertise, allowing to successfully execute lease transactions. We assist airlines, financial institutions and leasing companies when selling or purchasing aircraft.</p>
  </section>
</body>
</html>
```